Amber Burrows Business Card Design

Amber Burrows - Gathering Gentle Meadow Corners

Amber Burrows is a company that focuses on promoting the design, construction, consultation and support of natural, creative and organic play spaces for Early Childhood and learning environments.

We need a professional Business Card designed that is unique modern and creative. The Philosophy of the company is nostalgic so the business and will need to reflect this but also reflect that our ideas are modern and cutting edge.

The business card will need to be a talking point, by either having a unique size, quality and/or placement of logo or other quality.

I am more interested in using natural recycled paper, as this would reflect the philosophy of the company, but I open to seeing colour used creatively.
Updates

Hi Designers, Apologies, Could you please add www.amberburrows.com.au to the business card. Thanks very much.

Hi All, Thank you all for your submission thus far. Please note the fonts for used in the logo are: Ostrich Sans Black and Archer Semi Bold. If these could be considered for contact details, my name etc. Also please show the design on a recycled brown card if possible as this will be the type of card I will use when printing. Thanks so much.

Target Market(s)

Child Care Providers, Play Industry Professionals

Industry/Entity Type

Business

Contact Information for Business Card

Amber Burrows
Gathering Gentle Meadow Corners
Marguerite Holloway
0419 862 503
marguerite@amberburrows.com.au

Font styles to use
Sans Serif

Requirements
Must have
• The Logo and the Details plus the below phrase
• Amber Burrows - Gathering Gentle Meadow Corners
Nice to have
• A bit of colour, but not too much colour.
Should not have
• Not to have a white background, recycled brown card only

```html
<!DOCTYPE html>
<html lang="en">
<head>
<meta charset="utf-8">
<title>Amber Burrows Business Card Design</title>
<link href="https://fonts.googleapis.com/css2?family=Arvo:wght@400;700&family=Open+Sans:wght@400;600;700&display=swap" rel="stylesheet">
<style>
  :root {
    --page: #e9e6e1;
    --ink: #0b0b0b;
    --paper: #ffffff;
    --paper-shade: #f1f1f1;
    --light-text: #ffffff;
    --card-shadow: rgba(0, 0, 0, 0.22);
  }
  * { box-sizing: border-box; margin: 0; padding: 0; }
  html, body {
    width: 1200px;
    height: 900px;
    overflow: hidden;
    background: var(--page);
    font-family: "Open Sans", Arial, sans-serif;
  }
  .canvas { position: relative; width: 1200px; height: 900px; }

  .card {
    position: absolute;
    width: 620px;
    height: 378px;
    overflow: hidden;
    box-shadow: 0 10px 28px var(--card-shadow);
  }

  /* Back of card */
  .card--back {
    left: 90px;
    top: 66px;
    background: var(--ink);
    color: var(--light-text);
    display: flex;
    align-items: center;
    justify-content: center;
  }
  .brand { display: flex; flex-direction: column; align-items: center; }
  .brand__row { display: flex; align-items: center; gap: 14px; }
  .brand__dot {
    width: 34px; height: 34px; border-radius: 50%;
    background: currentColor;
  }
  .brand__name {
    font-family: "Open Sans", Arial, sans-serif;
    font-weight: 700;
    font-size: 40px;
    letter-spacing: 1px;
    text-transform: uppercase;
    line-height: 1;
  }
  .brand__tagline {
    margin-top: 10px;
    font-family: "Arvo", Georgia, serif;
    font-size: 14px;
    letter-spacing: 1.5px;
    text-transform: uppercase;
    text-align: center;
    line-height: 1.2;
  }

  /* Front of card */
  .card--front {
    left: 490px;
    top: 460px;
    background: var(--ink);
  }
  .front__top {
    position: absolute; left: 0; top: 0; right: 0; height: 190px;
    background: linear-gradient(180deg, var(--paper) 60%, var(--paper-shade));
    color: var(--ink);
    display: flex; align-items: center; justify-content: center;
  }
  .front__top .brand__name { font-size: 34px; }
  .front__top .brand__dot { width: 28px; height: 28px; }
  .front__top .brand__tagline { font-size: 12px; }

  .front__bottom {
    position: absolute; left: 0; right: 0; top: 190px; bottom: 0;
    color: var(--light-text);
  }
  .holder {
    position: absolute; right: 40px; top: 30px;
    font-weight: 700; font-size: 19px;
  }
  .contacts {
    position: absolute; right: 250px; top: 34px;
    list-style: none;
    display: flex; flex-direction: column; align-items: flex-end; gap: 12px;
    font-size: 15px;
  }
  .contacts li { display: flex; align-items: center; gap: 8px; }
  .contacts svg { width: 14px; height: 14px; fill: var(--light-text); flex: none; }
</style>
</head>
<body>
<main class="canvas">

  <section class="card card--back" aria-label="Card back">
    <div class="brand">
      <div class="brand__row">
        <span class="brand__dot" aria-hidden="true"></span>
        <span class="brand__name">Amber Burrows</span>
      </div>
      <p class="brand__tagline">Gathering<br>Gentle Meadow Corners</p>
    </div>
  </section>

  <section class="card card--front" aria-label="Card front">
    <div class="front__top">
      <div class="brand">
        <div class="brand__row">
          <span class="brand__dot" aria-hidden="true"></span>
          <span class="brand__name">Amber Burrows</span>
        </div>
        <p class="brand__tagline">Gathering<br>Gentle Meadow Corners</p>
      </div>
    </div>

    <div class="front__bottom">
      <p class="holder">Marguerite Holloway</p>
      <ul class="contacts">
        <li>0419 862 503
          <svg viewBox="0 0 24 24" aria-hidden="true"><path d="M6.6 10.8a15.1 15.1 0 0 0 6.6 6.6l2.2-2.2a1 1 0 0 1 1-.25 11.4 11.4 0 0 0 3.6.57 1 1 0 0 1 1 1V20a1 1 0 0 1-1 1A17 17 0 0 1 3 4a1 1 0 0 1 1-1h3.5a1 1 0 0 1 1 1c0 1.25.2 2.45.57 3.57a1 1 0 0 1-.25 1z"/></svg>
        </li>
        <li>marguerite@amberburrows.com.au
          <svg viewBox="0 0 24 24" aria-hidden="true"><path d="M2 5h20v14H2z M4 7v.4l8 5.2 8-5.2V7z" fill-rule="evenodd"/></svg>
        </li>
        <li>www.amberburrows.com.au
          <svg viewBox="0 0 24 24" aria-hidden="true"><path d="M12 2a10 10 0 1 0 0 20 10 10 0 0 0 0-20zm0 2c.9 1.2 1.6 2.6 2 4h-4c.4-1.4 1.1-2.8 2-4zM4.3 14a8 8 0 0 1 0-4h3.4a16 16 0 0 0 0 4zm.9 2h3c.3 1.3.8 2.5 1.4 3.6A8 8 0 0 1 5.2 16zm3-8h-3a8 8 0 0 1 4.4-3.6C8.9 5.5 8.5 6.7 8.2 8zM12 20c-.9-1.2-1.6-2.6-2-4h4c-.4 1.4-1.1 2.8-2 4zm2.3-6H9.7a14 14 0 0 1 0-4h4.6a14 14 0 0 1 0 4zm.1 5.6c.6-1.1 1.1-2.3 1.4-3.6h3a8 8 0 0 1-4.4 3.6zM16.3 14a16 16 0 0 0 0-4h3.4a8 8 0 0 1 0 4z"/></svg>
        </li>
      </ul>
    </div>
  </section>

</main>
</body>
</html>
```